Wine Bottle Label for Tall Fern Cellars

We are a small, newly established winery in need of an original, bold and outstanding bottle label design for our Tall Fern wine.

Our vineyard and winery are located on a 200 acre farm in a remote part of southern Oregon. The name "Tall Fern" was inspired by the large, overgrown size of all of the foliage here, including our grapevines. Things grow large and vigorous in Oregon! And everything is very lush and green. It is almost surreal or other-worldly, like the landscapes seen in the Keeper of The Hollows movies, or the land of Yarrowmere. It is a place that makes you say "wow" with its epic, large scale, natural beauty.

The name "Tall Fern" also captures the essence of our wine. It is big in flavor, quality and color. Our first release is a Pinot Noir (red). Pinot Noir wines often are subtle in flavor and thin in their color. Our label should convey that our Pinot Noir is a much more robust, darker, heavier, meatier, more flavorful wine that is a lot more fun than an "ordinary" wine. At the same time, this wine is not cheap, and so nothing in the label should convey "bargain," "low price," or "cheapness." This is a fine wine with a sense of adventure. Be sure to convey "quality" with your design along with "big," "adventure" and "fun".

The label should appeal to a younger demographic, both male and female, between the ages of 21 and 35. It should be non-traditional and adventurous and suggest a pushing of boundaries and a breaking of rules. This Pinot Noir does not conform to the normal "limitations" of the variety, therefore the label should not conform. It should have an "organic" or "natural" or "agricultural" vibe, as opposed to something mechanical or technical. It should, however, be contemporary. Do not confuse "natural" or "organic" with being nostalgic or old school. Think "agri-hipsters."

The label should be designed to fit on a Burgundy-style wine bottle (photo attached for reference). (Note: All Pinot Noir and Chardonnay is bottled in Burgundy bottles, If you are not sure about the bottle shape you can go to a local store and compare the various bottles. Locate a bottle of Pinot Noir or Chardonnay or anything identified as a "Burgundy Wine," and it should be the correct bottle. The tall, skinny bottles used for Cabernet Sauvignon are NOT correct)). Please see the "Must Have" notes for more on the bottle.

In summary, the final project should be a wine bottle label design that conveys bigness, vastness, adventurous, non-traditional, high quality wine. A good tagline to keep in mind is "Living Large."

Target Market(s)

Young, hip, non-conformist wine drinkers aged 21-35 with a sense of adventure and an appreciation of quality.

Industry/Entity Type

School

Requirements
Must have
• *Must contain the words:

Tall Fern (the brand)
2013 Pinot Noir (the vintage year and variety)

*The label must be designed to fit a Burgundy-style wine bottle. A photo is attached for reference.

*Additionally, the label needs to fit on the lower, widest part of the bottle. The label will be printed on sticky paper and rolled onto the bottle with a machine. The machine cannot apply labels to the neck of the bottle. The maximum size of a label that will fit this space is 5.5 inches wide by 4.5 inches tall. You DO NOT have to fill ALL of this space or confine the label shape to a rectangle, but the label cannot exceed this size or it won't stick to the bottle properly. It will really help if you can put your hands on an actual bottle to see the logistics of applying the label. But if that is not possible, just do your best with the instructions you have. I am confident the winning design could be adjusted to fit the bottle, if necessary
Nice to have
• *Wine grape leaf or leaves.

*A concept I have been playing with is sunlight shining through leaves like light through a Kessler lamp or a stained glass window. This is NOT a requirement for this label. However, if the concept inspires and idea, I would be most happy to see it.
Should not have
• IF a leaf or leaves are included in the design (not a requirement) they MUST be wine grapevine leafs and preferably leaves of the Pinot Noir vine. Do not use generic leaves or identifiable leaves such as oak leaves, maple leaves, or anything that looks like the Canadian flag or the Dunmore Ice Hawks hockey logo. Reference the attached photos of wine grape leaves to see the correct leaf type. I am happy to email more photos upon request. These photos may be used in whole or in part in your design, however, a leaf from a photo is NOT a requirement, nor is the image of a leaf or leaves.

This label should NOT be designed for Bordeaux-style wine bottles (the tall, skinny ones).

```html
<!DOCTYPE html>
<html lang="en">
<head>
<meta charset="utf-8">
<title>Tall Fern Cellars — 2013 Pinot Noir Label</title>
<link rel="stylesheet" href="https://fonts.googleapis.com/css2?family=Alegreya:wght@500;700&family=Alegreya+SC:wght@500&display=swap">
<style>
  :root {
    --canvas: #ffffff;
    --band: #1c1a1b;
    --paper: #ffffff;
    --ink: #141414;
    --leaf-deep: #2f8a12;
    --leaf-mid: #4fa91c;
    --leaf-light: #a9dd4a;
    --leaf-pale: #d8f2a4;
    --rule: #2a2a2a;
  }
  * { box-sizing: border-box; margin: 0; padding: 0; }
  html, body {
    width: 1200px; height: 1000px; overflow: hidden;
    background: var(--canvas);
  }
  .label {
    position: absolute;
    left: 200px; top: 172px;
    width: 801px; height: 655px;
    background: var(--paper);
    overflow: hidden;
  }
  .label__band {
    position: absolute; left: 0; width: 100%;
    background: var(--band);
  }
  .label__band--top { top: 0; height: 57px; }
  .label__band--bottom { bottom: 0; height: 55px; }

  .foliage {
    position: absolute;
    border-radius: 40px;
    background: radial-gradient(circle at 40% 40%, var(--leaf-pale), var(--leaf-light) 40%, var(--leaf-mid) 75%, rgba(79,169,28,0) 100%);
    opacity: .55;
  }
  .foliage--left-top { left: -30px; top: 57px; width: 150px; height: 250px; }
  .foliage--left-low { left: -40px; top: 380px; width: 110px; height: 150px; }
  .foliage--top { left: 330px; top: 57px; width: 230px; height: 35px; border-radius: 0 0 30px 30px; }
  .foliage--right-top { left: 610px; top: 57px; width: 200px; height: 170px; }
  .foliage--right-low { left: 690px; top: 300px; width: 140px; height: 250px; }
  .foliage--bottom { left: -10px; top: 540px; width: 170px; height: 60px; border-radius: 30px 30px 0 0; }

  .brand {
    position: absolute; left: 0; top: 88px; width: 100%;
    text-align: center;
    font-family: "Alegreya", Georgia, serif;
    font-weight: 700;
    font-size: 210px;
    line-height: 184px;
    letter-spacing: -4px;
    background: linear-gradient(160deg, var(--leaf-mid) 0%, var(--leaf-deep) 45%, var(--leaf-light) 70%, var(--leaf-deep) 100%);
    -webkit-background-clip: text; background-clip: text;
    color: transparent;
  }
  .brand__line { display: block; }
  .brand__line--top { margin-left: 30px; }

  .vintage {
    position: absolute; left: 0; top: 488px; width: 100%;
    text-align: center;
    font-family: "Alegreya", Georgia, serif;
    font-weight: 500; font-size: 36px; color: var(--ink);
  }
  .label__rule {
    position: absolute; left: 0; top: 528px; width: 100%;
    height: 1.5px; background: var(--rule);
  }
  .variety {
    position: absolute; left: 0; top: 534px; width: 100%;
    text-align: center;
    font-family: "Alegreya SC", Georgia, serif;
    font-weight: 500; font-size: 40px; letter-spacing: 1px; color: var(--ink);
  }
</style>
</head>
<body>
  <section class="label" aria-label="Tall Fern 2013 Pinot Noir wine label">
    <div class="label__band label__band--top"></div>

    <div class="foliage foliage--left-top" role="img" aria-label="Sunlit vine leaf texture in scattered letterforms"></div>
    <div class="foliage foliage--left-low" role="img" aria-label="Sunlit vine leaf texture in scattered letterforms"></div>
    <div class="foliage foliage--top" role="img" aria-label="Sunlit vine leaf texture in scattered letterforms"></div>
    <div class="foliage foliage--right-top" role="img" aria-label="Sunlit vine leaf texture in scattered letterforms"></div>
    <div class="foliage foliage--right-low" role="img" aria-label="Sunlit vine leaf texture in scattered letterforms"></div>
    <div class="foliage foliage--bottom" role="img" aria-label="Sunlit vine leaf texture in scattered letterforms"></div>

    <h1 class="brand">
      <span class="brand__line brand__line--top">Tall</span>
      <span class="brand__line">Fern</span>
    </h1>

    <p class="vintage">2013</p>
    <div class="label__rule"></div>
    <p class="variety">Pinot Noir</p>

    <div class="label__band label__band--bottom"></div>
  </section>
</body>
</html>
```